Poster for a new "Pizza Roll" Combo at our bakery

We are a cinnamon roll and coffee focused bakery, but we would like an innovative poster design to bring attention to our new offering, a Pizza Roll. We will be offering it as a combo, and this is what we wish to advertise. It will be geared mainly towards a younger high school aged crowd. I have included pics of the Pizza Rolls, but it's up to you how you want to incorporate them in the design.Poster should include our logo, the pizza rolls, and can include a drink to illustrate the combo as well. ( we offer710 ml vima bottle products and lurn bottled waters)Main Text: Try our amazing new Pizza Rolls! Message to get accross: $6.00 for a Pizza Roll and drink.Small Print: Avail after 11am, while supplies last. Includes one pizza roll and one bottled drink of choice. Taxes extra.

Target Market(s)

Broad, but mainly high school aged kids

Industry/Entity Type

Bakery

Colors

Designer to choose colors to be used in the design.

Requirements
Must have
• Text: " Try our amazing new PIzza Rolls!:
• $6 Pizza Roll Combo (Pizza Roll and a drink)
Nice to have
• Pic of the PIzza Roll (photo shopped if needed to improve esthetics)
• Pic of a Bottled 710ml vima drink
Should not have
• Any animal product references, as we are a Vegan shop.

```html
<!DOCTYPE html>
<html lang="en">
<head>
<meta charset="utf-8">
<title>Pizza Roll Combo Poster</title>
<link rel="stylesheet" href="https://fonts.googleapis.com/css2?family=Montserrat:wght@400;500;800;900&family=Oswald:wght@500;600&display=swap">
<style>
  :root {
    --ink: #231f20;
    --purple: #6e5899;
    --yellow: #f5b335;
    --white: #ffffff;
    --crust-light: #e9ddc9;
    --crust-gold: #d58a2c;
    --sauce: #b9642a;
  }
  * { margin: 0; padding: 0; box-sizing: border-box; }
  html, body { width: 800px; height: 1200px; overflow: hidden; background: var(--ink); }
  .poster {
    position: relative; width: 800px; height: 1200px; overflow: hidden;
    background: var(--ink); color: var(--white);
    font-family: "Montserrat", Arial, sans-serif;
  }
  .ribbon { position: absolute; left: 178px; top: 38px; width: 444px; height: 64px; }
  .ribbon-text {
    position: absolute; left: 178px; top: 38px; width: 444px; height: 64px;
    display: flex; align-items: center; justify-content: center;
    font-weight: 900; font-size: 34px; letter-spacing: 1px; color: var(--white);
  }
  .product-photo {
    position: absolute; left: 228px; top: 166px; width: 352px; height: 306px;
    border-radius: 48% 52% 44% 46% / 40% 40% 58% 58%;
    background: radial-gradient(ellipse at 48% 28%, var(--sauce) 0%, var(--crust-gold) 32%, var(--crust-light) 62%, #c9b79c 100%);
  }
  .combo-badge {
    position: absolute; left: 566px; top: 144px; width: 152px; height: 152px;
    border-radius: 50%; background: var(--yellow);
    display: flex; align-items: center; justify-content: center; text-align: center;
    font-family: "Oswald", "Arial Narrow", sans-serif; font-weight: 500;
    font-size: 31px; line-height: 1.02; color: var(--white); padding-bottom: 8px;
  }
  .price-tag {
    position: absolute; left: 550px; top: 282px; width: 186px; height: 72px;
    background: var(--purple); transform: rotate(5deg);
    display: flex; align-items: center; justify-content: center;
    font-family: "Oswald", "Arial Narrow", sans-serif; font-weight: 600;
    font-size: 40px; color: var(--white);
  }
  .lead {
    position: absolute; left: 0; width: 800px; text-align: center;
    font-weight: 400; font-size: 58px; letter-spacing: 4px; line-height: 1;
  }
  .lead-1 { top: 494px; }
  .lead-2 { top: 558px; }
  .headline {
    position: absolute; left: 0; width: 800px; text-align: center;
    font-weight: 900; line-height: 1;
  }
  .headline-pizza { top: 636px; font-size: 120px; letter-spacing: 6px; color: var(--yellow); }
  .headline-rolls { top: 735px; font-size: 140px; letter-spacing: 2px; color: var(--purple); }
  .rule-set { position: absolute; top: 678px; width: 88px; height: 42px; }
  .rule-left { left: 102px; }
  .rule-right { left: 638px; }
  .fine-print {
    position: absolute; left: 0; top: 910px; width: 800px; text-align: center;
    font-weight: 400; font-size: 23.5px; line-height: 34px;
  }
  .footer { position: absolute; left: 0; top: 1000px; width: 800px; height: 200px; }
  .brand-mark {
    position: absolute; left: 70px; top: 1058px; width: 120px; height: 120px;
    border-radius: 50%; background: var(--ink); border: 2px solid var(--white);
    display: flex; flex-direction: column; align-items: center; justify-content: center;
  }
  .brand-name { font-weight: 500; font-size: 21px; color: var(--white); }
  .brand-tagline { font-weight: 500; font-size: 7px; color: var(--white); margin-top: 4px; }
  .social-links {
    position: absolute; left: 596px; top: 1070px; width: 184px;
    display: flex; justify-content: space-between;
    font-weight: 500; font-size: 14px; color: var(--white);
  }
  .web-address {
    position: absolute; left: 430px; top: 1122px; width: 340px; text-align: center;
    font-weight: 400; font-size: 21px; letter-spacing: 5px; color: var(--white);
  }
</style>
</head>
<body>
<main class="poster">
  <svg class="ribbon" viewBox="0 0 444 64" aria-hidden="true">
    <polygon points="0,0 444,0 420,32 444,64 0,64 24,32" fill="var(--purple)"/>
  </svg>
  <div class="ribbon-text">SPECIAL OFFER</div>

  <div class="product-photo" role="img" aria-label="Photo of a baked vegan pizza roll swirl with tomato sauce"></div>

  <div class="combo-badge">PIZZA ROLL<br>&amp; DRINK</div>
  <div class="price-tag">ONLY $6</div>

  <p class="lead lead-1">TRY OUR</p>
  <p class="lead lead-2">AMAZING NEW</p>

  <svg class="rule-set rule-left" viewBox="0 0 88 42" aria-hidden="true">
    <g stroke="var(--purple)" stroke-width="1.5"><line x1="0" y1="4" x2="88" y2="4"/><line x1="0" y1="21" x2="88" y2="21"/><line x1="0" y1="38" x2="88" y2="38"/></g>
  </svg>
  <svg class="rule-set rule-right" viewBox="0 0 88 42" aria-hidden="true">
    <g stroke="var(--purple)" stroke-width="1.5"><line x1="0" y1="4" x2="88" y2="4"/><line x1="0" y1="21" x2="88" y2="21"/><line x1="0" y1="38" x2="88" y2="38"/></g>
  </svg>
  <h1 class="headline headline-pizza">PIZZA</h1>
  <h1 class="headline headline-rolls">ROLLS!</h1>

  <p class="fine-print">Available after 11am, while supplies last.<br>Includes one pizza roll and one bottled drink of choice.<br>Taxes extra.</p>

  <svg class="footer" viewBox="0 0 800 200" aria-hidden="true">
    <polygon points="254,92 800,12 800,200 254,200" fill="var(--purple)"/>
    <polygon points="8,68 126,32 254,68 254,200 8,200" fill="var(--yellow)"/>
  </svg>
  <div class="brand-mark">
    <span class="brand-name">Rollvana</span>
    <span class="brand-tagline">Gourmet Vegan Rolls</span>
  </div>
  <nav class="social-links"><span>Plimzo</span><span>Quorfa</span><span>Tweezlo</span></nav>
  <p class="web-address">www.rollvana.com</p>
</main>
</body>
</html>
```